Website for Fernvale Harmony Chapel

Wordpress website design required for Fernvale Harmony Chapel. We are a family oriented church catering for age groups from school age to elderly people. The church has a wide variety of activities which it coordinates. The idea is to describe the activities on the activities page, but cross-link them to show which would be applicable to the different age groups.

We would like an inviting website which is easy to read and navigate.

Target Market(s)

Very wide audience - from school age youth to elderly people, so design and style should cater for both audiences.

Industry/Entity Type

Church

Coding

Coded - Design and coding required

Number of Pages Required

5+ page

Font styles to use
Sans Serif

Colors
0255a3
ffffff
0792cd
f78f20

Requirements
Must have
• Inviting website.
• Clear readable font.
• Space to import photos to balance text on each page.
• Need to project a dynamic and progressive feel for the church.
• Easy to navigate.
Nice to have
• Scrolling photos on pages. Ability to enter questions/ comments/prayer requests on Home page.
Should not have
• Conservative audience, so should not be too bold.

```html
<!DOCTYPE html>
<html lang="en">
<head>
<meta charset="utf-8">
<title>Fernvale Harmony Chapel</title>
<link rel="stylesheet" href="https://fonts.googleapis.com/css2?family=Roboto:wght@300;400;500;700&family=Montserrat:wght@400;600;700&family=Noto+Serif:wght@400;700&display=swap">
<style>
:root{
  --gold:#a8913f;
  --gold-dark:#8c7a34;
  --navy:#0d2b5c;
  --yellow:#fcc462;
  --cream:#f8f0e4;
  --brown:#3a2c28;
  --ink:#2b2b2b;
  --muted:#6b5a4a;
  --orange:#d9761f;
  --white:#ffffff;
}
*{box-sizing:border-box;margin:0;padding:0}
html,body{width:1200px;height:2903px;overflow:hidden}
body{font-family:"Noto Serif",serif;color:var(--ink);background:var(--white);position:relative}
section,header,footer{position:absolute;left:0;width:1200px}
.abs{position:absolute}
.btn{position:absolute;display:flex;align-items:center;justify-content:center;background:var(--yellow);color:#3a2a10;font-family:"Roboto",sans-serif;font-weight:500;text-transform:uppercase;font-size:15px}

/* header */
.site-header{top:0;height:74px;background:var(--white)}
.brand{left:128px;top:26px;display:flex;align-items:center;gap:8px;font-family:"Roboto",sans-serif;font-size:15px;font-weight:500;color:var(--navy)}
.brand-dot{width:14px;height:14px;border-radius:50%;background:var(--gold)}
.main-nav{right:126px;top:28px;display:flex;gap:30px;font-family:"Roboto",sans-serif;font-size:15px;color:#222;text-transform:uppercase}

/* hero */
.hero{top:74px;height:526px;background:radial-gradient(ellipse at 50% 35%,#6a564c 0%,#3e302b 45%,#241b18 100%)}
.hero-photo{left:0;top:0;width:1200px;height:526px}
.hero-title{left:0;width:1200px;top:136px;text-align:center;font-family:"Roboto",sans-serif;color:var(--white);font-size:74px;line-height:78px}
.hero-title strong{display:block;font-weight:700}
.hero-title span{display:block;font-weight:300}
.hero-text{left:0;width:1200px;top:290px;text-align:center;font-family:"Roboto",sans-serif;font-size:15px;line-height:20px;color:#f0e8e0}
.hero .btn{left:494px;top:350px;width:213px;height:46px}

/* event band */
.event-band{top:600px;height:108px;background:var(--gold)}
.event-label{left:128px;top:26px;font-family:"Roboto",sans-serif;font-weight:700;font-size:17px;color:var(--white)}
.event-title{left:128px;top:50px;font-family:"Roboto",sans-serif;font-weight:500;font-size:22px;color:var(--white)}
.event-band .btn{left:855px;top:31px;width:215px;height:48px;background:var(--navy);color:var(--white);font-weight:700}

/* features */
.features{top:708px;height:401px}
.feature{position:absolute;top:50px;width:310px}
.feature-photo{width:310px;height:167px}
.feature h3{margin-top:24px;font-family:"Montserrat",sans-serif;font-size:15px;font-weight:700;color:#222}
.feature p{margin-top:12px;font-size:12.5px;line-height:19px;color:var(--muted)}
.feature a{display:block;margin-top:8px;font-size:13px;color:#222;text-decoration:none}

/* programs */
.programs{top:1109px;height:315px;background:var(--cream)}
.section-title{font-family:"Montserrat",sans-serif;font-weight:700;font-size:17px;color:#333;text-transform:uppercase}
.section-title::after{content:"";display:block;width:30px;height:3px;background:#555;margin-top:10px}
.programs .section-title{left:0;width:1200px;top:36px;text-align:center}
.programs .section-title::after{margin:10px auto 0}
.program{position:absolute;top:112px;width:240px;text-align:center}
.program .date{font-family:"Montserrat",sans-serif;font-weight:600;font-size:17px;color:#222}
.program .date::after{content:"";display:block;width:16px;height:2px;background:#555;margin:8px auto 0}
.program .name{margin-top:8px;font-size:16px;color:#333}
.program .time{margin-top:10px;font-size:12.5px;color:#555}
.program .btn{position:relative;margin:14px auto 0;width:88px;height:28px;font-size:12px}
.arrow{top:150px}
.dots{left:0;width:1200px;display:flex;justify-content:center;gap:6px}
.dots i{width:8px;height:8px;border-radius:50%;background:#d6c8b4}
.dots i.on{background:#b28a5a}

/* bulletin */
.bulletin{top:1424px;height:484px}
.bulletin .section-title{left:130px;top:36px}
.post{position:absolute;left:130px;width:700px;height:149px}
.post-photo{position:absolute;left:0;top:0;width:224px;height:149px}
.post-body{position:absolute;left:249px;top:0;width:451px}
.post h4{font-family:"Montserrat",sans-serif;font-weight:600;font-size:17px;color:#222}
.post .meta{margin-top:5px;font-size:12px;color:var(--orange)}
.post .meta b{font-weight:400;color:var(--orange)}
.post p{margin-top:8px;font-size:12.5px;line-height:19px;color:#555}
.post .btn{position:relative;margin-top:8px;width:128px;height:28px;font-size:12px}
.sermons{left:848px;top:25px;width:222px;height:438px;background:var(--cream)}
.sermons .section-title{position:absolute;left:0;width:222px;top:24px;text-align:center;font-size:16px}
.sermons .section-title::after{margin:10px auto 0}
.sermon-video{left:17px;top:77px;width:188px;height:121px}
.sermon-list{left:17px;top:210px;width:188px;list-style:none}
.sermon-list li{padding:6px 0 6px 16px;border-bottom:1px solid #e6dccd;position:relative;font-size:12px;color:#333;height:54px}
.sermon-list li::before{content:"";position:absolute;left:0;top:10px;border-left:8px solid #555;border-top:5px solid transparent;border-bottom:5px solid transparent}
.sermon-list li span{display:block;margin-top:6px;color:var(--orange);font-size:12px}
.sermon-list li:last-child{border-bottom:0}

/* prayer */
.prayer{top:1908px;height:194px;background:linear-gradient(90deg,#2f2420,#4a3a32 50%,#2f2420)}
.prayer h2{left:149px;top:76px;font-family:"Roboto",sans-serif;font-weight:400;font-size:24px;color:var(--white)}
.prayer p{left:149px;top:110px;font-style:italic;font-size:14px;color:#eee}
.prayer .btn{left:753px;top:77px;width:259px;height:47px}

/* verses */
.verses{top:2102px;height:309px;background:var(--cream)}
.verses .section-title{left:0;width:1200px;top:36px;text-align:center}
.verses .section-title::after{margin:10px auto 0}
.quote{left:170px;width:860px;top:115px;text-align:center;font-size:23px;line-height:38px;color:#333}
.quote-ref{left:0;width:1200px;top:200px;text-align:center;font-size:17px;color:#555}
.qmark{font-family:"Noto Serif",serif;font-size:90px;color:#d9cdbb;line-height:1}

/* contact */
.contact{top:2411px;height:492px}
.contact-left{left:0;top:0;width:551px;height:492px;background:var(--gold)}
.contact-right{left:551px;top:0;width:649px;height:492px;background:linear-gradient(135deg,#4e3e34,#2a201c)}
.contact h2{left:160px;top:82px;font-family:"Roboto",sans-serif;font-weight:500;font-size:54px;line-height:54px;color:var(--white)}
.contact-info{left:160px;top:248px;font-family:"Roboto",sans-serif;color:var(--white)}
.contact-info dt{font-size:16px;font-weight:500;margin-top:20px}
.contact-info dd{font-size:12.5px;font-weight:500;margin-top:4px;line-height:17px}
.rule{left:160px;top:385px;width:112px;height:3px;background:var(--yellow)}
.copyright{left:160px;top:437px;font-family:"Roboto",sans-serif;font-size:12.5px;color:var(--white)}
.field{position:absolute;left:578px;width:463px;border-bottom:3px solid var(--white);font-family:"Roboto",sans-serif;font-weight:500;font-size:16px;color:var(--white);text-transform:uppercase}
.send{left:845px;top:418px;width:161px;height:44px;border:2px solid #bdb3aa;display:flex;align-items:center;justify-content:center;gap:14px;font-family:"Roboto",sans-serif;font-size:14px;color:var(--white)}
</style>
</head>
<body>

<header class="site-header">
  <div class="abs brand"><span class="brand-dot"></span>Fernvale Harmony Chapel</div>
  <nav class="abs main-nav">
    <span>Our Product</span><span>Age Group</span><span>Activites</span><span>Events</span><span>About</span><span>Contact</span>
  </nav>
</header>

<section class="hero">
  <div class="abs hero-photo" role="img" aria-label="Photo of hands clasped in prayer over an open Bible"></div>
  <h1 class="abs hero-title"><strong>LOVING GOD</strong><span>LOVING OTHERS</span></h1>
  <p class="abs hero-text">Lorem ipsum dolor sit amet, consectetuer adipiscing elit, sed diam<br>nonummy nibh euismod tincidunt ut laoreet dolore magna</p>
  <a class="btn">Learn more about us</a>
</section>

<section class="event-band">
  <div class="abs event-label">UPCOMING EVENT</div>
  <div class="abs event-title">"THE LAW DEMANDS, BUT GRACE SUPPLIES" - PASTOR D.K.</div>
  <a class="btn">Progaram Details</a>
</section>

<section class="features">
  <article class="feature" style="left:110px">
    <div class="feature-photo" role="img" aria-label="Photo of a hiker on a mountain ridge at sunset" style="background:linear-gradient(160deg,#f0b86a,#a05a2a 60%,#4a2a1a)"></div>
    <h3>GUIDED BY THE HOLY SPIRIT</h3>
    <p>Experience God's Wisdom each day as you are lead by the Holy Spirit. Walk effortlessly into success and happiness and understand the Father's love for you.</p>
    <a>View details →</a>
  </article>
  <article class="feature" style="left:445px">
    <div class="feature-photo" role="img" aria-label="Photo of a lifeguard tower on a beach" style="background:linear-gradient(180deg,#e8c9c0,#c9b8b4 50%,#9a8c88)"></div>
    <h3>LAW DEMANDS; GRACE SUPPLIES</h3>
    <p>Jesus came and fulfilled the laws, the only one who could keep the laws so that in Him we can be made righteous and not have to suffer death for our sins.</p>
    <a>View details →</a>
  </article>
  <article class="feature" style="left:780px">
    <div class="feature-photo" role="img" aria-label="Photo of a person standing on a rocky shore at sunset" style="background:linear-gradient(180deg,#f2d3a8,#c98a5a 55%,#5a3a2a)"></div>
    <h3>CHRIST OCCUPIED</h3>
    <p>It may sound good to Mankind to be self-occupied. But God wants you to be Christ-Occupied and receive all of your blessings through resting in the work of Jesus.</p>
    <a>View details →</a>
  </article>
</section>

<section class="programs">
  <h2 class="abs section-title">Programs &amp; Events</h2>
  <svg class="abs arrow" style="left:96px" width="18" height="30" viewBox="0 0 18 30"><path d="M15 2 3 15l12 13" fill="none" stroke="#555" stroke-width="2"/></svg>
  <svg class="abs arrow" style="left:1080px" width="18" height="30" viewBox="0 0 18 30"><path d="M3 2l12 13L3 28" fill="none" stroke="#555" stroke-width="2"/></svg>
  <div class="program" style="left:108px"><div class="date">JULY 16</div><div class="name">Weekly meeting &amp; prayer</div><div class="time">Monday 07:00 AM</div><a class="btn">Details →</a></div>
  <div class="program" style="left:354px"><div class="date">JUL 29</div><div class="name">Show me your faith</div><div class="time">Thursday 02:00 PM</div><a class="btn">Details →</a></div>
  <div class="program" style="left:602px"><div class="date">SEP 19</div><div class="name">Perseravance of the saints</div><div class="time">Saturday 10:00 AM</div><a class="btn">Details →</a></div>
  <div class="program" style="left:848px"><div class="date">OCT 14</div><div class="name">God's irresistable grace</div><div class="time">Sunday 11:00 AM</div><a class="btn">Details →</a></div>
  <div class="abs dots" style="top:262px"><i class="on"></i><i></i></div>
</section>

<section class="bulletin">
  <h2 class="abs section-title">Latest Bulletin</h2>
  <article class="post" style="top:105px">
    <div class="post-photo" role="img" aria-label="Photo of pink flowers in bloom" style="background:linear-gradient(135deg,#f29a7a,#e0604a 55%,#7a3a2a)"></div>
    <div class="post-body">
      <h4>Perseverance of the Saints</h4>
      <div class="meta">on 17th June 2014 by <b>Martin Hale</b></div>
      <p>Lorem ipsum dolor sit amet, consectetur adipiscing elit. Nulla convallis egestas rhoncus. Donec facilisis fermentum sem, ac viverra ante luctus vel. Donec vel mauris quam. Lorem ipsum dolor sit amet...</p>
      <a class="btn">Read Article →</a>
    </div>
  </article>
  <article class="post" style="top:298px">
    <div class="post-photo" role="img" aria-label="Photo of an old town street with buildings" style="background:linear-gradient(160deg,#c9c2b4,#8a8070 55%,#4a4438)"></div>
    <div class="post-body">
      <h4>Lord is Sufficient for all of our needs</h4>
      <div class="meta">on 17th June 2014 by <b>Owen Carter</b></div>
      <p>Lorem ipsum dolor sit amet, consectetur adipiscing elit. Nulla convallis egestas rhoncus. Donec facilisis fermentum sem, ac viverra ante luctus vel. Donec vel mauris quam. Lorem ipsum dolor sit amet...</p>
      <a class="btn">Read Article →</a>
    </div>
  </article>
  <aside class="abs sermons">
    <h2 class="section-title">Recent Sermons</h2>
    <div class="abs sermon-video" role="img" aria-label="Video still of a city at night" style="background:linear-gradient(180deg,#3a3a44,#1e1e24)"></div>
    <svg class="abs" style="left:86px;top:112px" width="52" height="52" viewBox="0 0 52 52"><circle cx="26" cy="26" r="24" fill="none" stroke="#fff" stroke-width="2.5"/><path d="M21 16v20l16-10z" fill="#fff"/></svg>
    <ul class="abs sermon-list">
      <li>Heavens and the earth<span>24:15 mins</span></li>
      <li>Prayer and petition<span>12:00 mins</span></li>
      <li>Fruit of the Spirit<span>30:25 mins</span></li>
      <li>Do not be afraid; keep on...<span>17:00 mins</span></li>
    </ul>
  </aside>
</section>

<section class="prayer" role="img" aria-label="Dark textured background photo">
  <h2 class="abs">Need Prayer? We Would Love To Pray For You.</h2>
  <p class="abs">We have a strong sense of community with parishioners.</p>
  <a class="btn">Send message for prayers</a>
</section>

<section class="verses">
  <h2 class="abs section-title">Bible Verses</h2>
  <div class="abs qmark" style="left:110px;top:70px">“</div>
  <div class="abs qmark" style="left:1040px;top:150px">”</div>
  <blockquote class="abs quote">For God so loved the world that he gave his one and only begotten Son, that who ever believes in him shall not perish but have eternal life.</blockquote>
  <div class="abs quote-ref">— John 3:16 (KJV)</div>
  <div class="abs dots" style="top:259px"><i class="on"></i><i></i><i></i></div>
</section>

<footer class="contact">
  <div class="abs contact-left" role="img" aria-label="Faint statue photo tinted gold"></div>
  <div class="abs contact-right" role="img" aria-label="Photo of a carved church statue"></div>
  <h2 class="abs">GET IN<br>TOUCH</h2>
  <dl class="abs contact-info">
    <dt>EMAIL</dt><dd>hello@fernvaleharmony.org</dd>
    <dt>PHONE</dt><dd>+1 (650) 555-0148<br>+1 (650) 555-0193</dd>
  </dl>
  <div class="abs rule"></div>
  <div class="abs copyright">Fernvale Harmony © 2016, All Right Reserved</div>
  <div class="field" style="top:84px;height:34px">Name</div>
  <div class="field" style="top:150px;height:34px">Email</div>
  <div class="field" style="top:214px;height:34px">Subject</div>
  <div class="field" style="top:280px;height:109px">Message</div>
  <div class="abs send">SEND <svg width="22" height="10" viewBox="0 0 22 10"><path d="M0 5h20M16 1l4 4-4 4" fill="none" stroke="#fff" stroke-width="1.5"/></svg></div>
</footer>

</body>
</html>
```